Bright Fern Custom Homes business card. Double sided. Modern. professional

Bright Fern Custom Homes
contemporary modern design with our logo /
Double sided with all our contact information
Use same Green colors as in our Logo. Contemporary logo that grabs your attention. Visually pleasing and balanced. Easy to read, and Vibrant. Would love an option for rounded edges. Embossed logo would be amazing.
Contact Information for Business Card
Dana Welk Owner / General Contractor Bright Fern Custom Homes p: 704.552.1830 m: 912.648.2071 e: brightferncustomhomes@mailbox.example w: www.brightferncustomhomes.example 218 Pryor Meadow Lane Ashwood, SC 29041

```html
<!DOCTYPE html>
<html lang="en">
<head>
<meta charset="utf-8">
<title>Bright Fern Custom Homes – Business Card</title>
<link rel="stylesheet" href="https://fonts.googleapis.com/css2?family=Cinzel:wght@400&family=Roboto+Condensed:wght@700&family=Roboto:wght@400&display=swap">
<style>
  :root{
    --backdrop:#3b3b3b;
    --paper:#ffffff;
    --ink-dark:#151515;
    --fern:#6b8a35;
    --fern-light:#7e9c3f;
    --text-gray:#555555;
  }
  *{box-sizing:border-box;margin:0;padding:0}
  html,body{width:1200px;height:801px;overflow:hidden}
  body{background:var(--backdrop);position:relative;font-family:"Roboto",Arial,sans-serif}

  .card{position:absolute;top:252px;width:520px;height:297px;border-radius:4px;overflow:hidden;box-shadow:0 10px 24px rgba(0,0,0,.35)}
  .card--front{left:50px;background:var(--paper);border-bottom:3px solid var(--fern)}
  .card--back{left:630px;background:var(--ink-dark);border-bottom:3px solid var(--fern)}

  .brand{display:flex;align-items:center;gap:10px}
  .brand__dot{width:14px;height:14px;border-radius:50%;background:var(--fern);flex:none}
  .brand__name{font-family:"Cinzel",Georgia,serif;font-weight:400;color:var(--fern);letter-spacing:.06em;line-height:1.15;white-space:nowrap}

  .card--front .brand{position:absolute;left:34px;top:150px;width:200px}
  .card--front .brand__name{font-size:17px}

  .divider{position:absolute;left:246px;top:78px;width:1px;height:128px;background:var(--fern)}

  .contact{position:absolute;left:264px;top:70px;color:var(--text-gray);font-size:11.5px;line-height:1.45}
  .contact__name{font-family:"Roboto Condensed",Arial,sans-serif;font-weight:700;font-size:18px;color:var(--fern);letter-spacing:.01em;line-height:1.1}
  .contact__title{margin-bottom:10px}
  .contact__address{margin-bottom:8px}
  .contact__row{display:flex;align-items:center;gap:6px;white-space:nowrap}
  .contact__row svg{width:10px;height:10px;flex:none;fill:var(--fern)}

  .card--back .brand{position:absolute;left:250px;top:150px}
  .card--back .brand__dot{width:20px;height:20px}
  .card--back .brand__name{font-size:22px;color:var(--fern-light)}
</style>
</head>
<body>

<section class="card card--front" aria-label="Card front">
  <div class="brand">
    <span class="brand__dot"></span>
    <span class="brand__name">Bright Fern<br>Custom Homes</span>
  </div>
  <div class="divider"></div>
  <div class="contact">
    <p class="contact__name">DANA WELK</p>
    <p class="contact__title">Owner / General Contractor</p>
    <p class="contact__address">218 Pryor Meadow Lane<br>Ashwood, SC 29041</p>
    <p class="contact__row">
      <svg viewBox="0 0 10 10" aria-hidden="true"><path d="M2 0.5 3.6 2.6 2.7 3.6C3.4 5 4.9 6.6 6.4 7.3L7.4 6.4 9.5 8 8.5 9.5C4.5 9.3.7 5.5.5 1.5Z"/></svg>
      704.552.1830
    </p>
    <p class="contact__row">
      <svg viewBox="0 0 10 10" aria-hidden="true"><path d="M2.5 0h5a1 1 0 0 1 1 1v8a1 1 0 0 1-1 1h-5a1 1 0 0 1-1-1V1a1 1 0 0 1 1-1Zm.3 1.2v6.6h4.4V1.2Z"/></svg>
      912.648.2071
    </p>
    <p class="contact__row">
      <svg viewBox="0 0 10 10" aria-hidden="true"><path d="M0 2h10v6H0Zm.8.7L5 5.6 9.2 2.7Z"/></svg>
      brightferncustomhomes@mailbox.example
    </p>
    <p class="contact__row">
      <svg viewBox="0 0 10 10" aria-hidden="true"><path d="M5 0a5 5 0 1 0 0 10A5 5 0 0 0 5 0Zm0 1a4 4 0 0 1 3.9 3.5H6.8C6.7 3 6.3 1.8 5.6 1Zm-.6 0C3.7 1.8 3.3 3 3.2 4.5H1.1A4 4 0 0 1 4.4 1ZM1.1 5.5h2.1c.1 1.5.5 2.7 1.2 3.5A4 4 0 0 1 1.1 5.5Zm3.1 0h1.6C5.7 6.9 5.4 8 5 8.7 4.6 8 4.3 6.9 4.2 5.5Zm2.6 0h2.1A4 4 0 0 1 5.6 9c.7-.8 1.1-2 1.2-3.5ZM4.2 4.5C4.3 3.1 4.6 2 5 1.3 5.4 2 5.7 3.1 5.8 4.5Z"/></svg>
      www.brightferncustomhomes.example
    </p>
  </div>
</section>

<section class="card card--back" aria-label="Card back">
  <div class="brand">
    <span class="brand__dot"></span>
    <span class="brand__name">Bright Fern<br>Custom Homes</span>
  </div>
</section>

</body>
</html>
```